Weather of the Heart Is the Ledger A Novel by Carl Whitby and Martin Holloway

Weather of the Heart Is the Ledger is a business novel about leadership, follower-ship, resilience, and insight.
It follows a high-performing executive whose conventional management tools and techniques stop working during a professional crisis. His transformation does not come from new strategies or tactics, but from a fundamentally different understanding of how mindset shapes performance, decision-making, leadership and follower-ship. Through the course of the book, the executive, his team, and his customers realize that “State of Mind” (healthy psychological functioning) is the horsepower that drives business and life.
This is not a self-help book, textbook, or memoir. It is thoughtful business fiction with philosophical depth.

Introduction/Preface for the novel:
We wrote this book because something profound changed the way we live, work, and lead. Over the course of several decades - across boardrooms, high-stakes corporate challenges, private practice, and moments of quiet personal insight - we began to see a deeper truth about the human experience. It was a truth that, once seen, dramatically improved the quality of our lives, and the lives of the people with whom we worked.
That truth comes from understanding the Three Principles of Mind, Consciousness, and Thought, as discovered and first articulated by the philosopher and theosopher, Edwin Thorley. Though simple, these Principles point to something universally powerful—how all people experience life from the inside out. When understood, they reveal a level of clarity, resilience, and well-being that can transform not only individuals, but entire organizations.
At first, we tried to write a traditional business book—a primer designed to share how understanding the Principles can lead to more grounded, wise, and effective leadership—without the need for techniques or tools. But as we wrote, we found ourselves returning again and again to stories. Real stories. Composite stories. Fictional ones. We realized that the best way to share this understanding wasn’t through frameworks or prescriptive advice. It was through story.
So, we created one big story.
This novel is the result. Though fictional, it is inspired by real patterns, real shifts, and real struggles we’ve lived through and witnessed over decades of work, together and separately. The characters are inventions, but their experiences are familiar. We’ve watched people just like them transform—from confusion to clarity, from fear to resilience, from burnout to wisdom.
Our hope is that this book moves you—not just as a story, but as an experience. We believe that the ideas woven into Owen Castell’s journey can help anyone live with greater ease, purpose, and peace of mind. Whether you lead a Fortune 500 company or a family of five, what’s offered here is for you.
And if something in this story helps you see your own life with fresh eyes, then the book has done its job.
Welcome to the journey.
—Carl & Martin

Target Market(s)

• Senior leaders, executives, and high-potential managers • Business professionals experiencing pressure, burnout, or diminishing returns from traditional leadership approaches • Leadership coaches and organizational consultants • Readers of intelligent, reflective business fiction or non-business people who are interested in what makes people tick — and achieve their highest potential Tone should appeal to serious, experienced professionals, not beginners or hype-seekers.

Industry/Entity Type

• Business / Leadership / Psychology • Business Fiction • Leadership Novel

Font styles to use
Serif

Colors
0054AA
0677BA
7BADD7
CADEEF
E8F1F8

Requirements
Must have
• We are looking for metaphorical representations of: • A fork in the road • A deviation from the conventional path (that makes all the difference) • One element choosing a different direction—not running away, not rebelling, just seeing differently Think quiet insight, not drama. Must-Haves • Clear, legible title at thumbnail size • A visual metaphor for choice or alternate thinking • Professional, credible aesthetic • Obvious that this is fiction (a novel), not a textbook • Clean typography (no clutter)
Nice to have
• • A sense of motion or transition • Minimalist or restrained color palette • One accent element that signifies insight or departure from convention • Timeless design (should still feel current in 5 or 10 years)
Should not have
• • Literal business clichés (gears, ladders, chess pieces, lightbulbs, compasses, eagles) • Stock-photo people in suits • “Hero CEO” imagery • Overly mystical or “woo-woo” visuals • Aggressive, macho, or hustle-culture tone • Anything cartoonish or silly

```html
<!DOCTYPE html>
<html lang="en">
<head>
<meta charset="utf-8">
<title>Weather of the Heart Is the Ledger — Cover</title>
<link rel="stylesheet" href="https://fonts.googleapis.com/css2?family=EB+Garamond:wght@400;500&display=swap">
<style>
  :root {
    --paper: #e7eef8;
    --paper-edge: #dfe7f3;
    --ink: #1f3a64;
    --channel-light: #c3d3e7;
    --channel-mid: #9bb4d2;
    --rule: #9fb2c9;
  }
  html, body {
    margin: 0;
    padding: 0;
    width: 800px;
    height: 1200px;
    overflow: hidden;
    background: var(--paper);
  }
  .cover {
    position: relative;
    width: 800px;
    height: 1200px;
    background: radial-gradient(ellipse at 50% 45%, #edf2fa 0%, var(--paper) 60%, var(--paper-edge) 100%);
  }
  .cover svg {
    position: absolute;
    inset: 0;
    display: block;
  }
  .title,
  .byline {
    font-family: "EB Garamond", "Garamond", serif;
    fill: var(--ink);
    font-weight: 500;
  }
  .title-line { letter-spacing: 0.04em; }
  .title-line--lead { font-size: 44px; }
  .title-line--joiner { font-size: 42px; letter-spacing: 0.08em; }
  .title-line--close { font-size: 72px; letter-spacing: 0.05em; }
  .byline { font-size: 56px; font-weight: 400; letter-spacing: 0.01em; }
</style>
</head>
<body>
<main class="cover">
  <svg width="800" height="1200" viewBox="0 0 800 1200" aria-labelledby="cover-title">
    <defs>
      <linearGradient id="channel-down" x1="0" y1="0" x2="0" y2="1">
        <stop offset="0" stop-color="var(--channel-mid)" stop-opacity="0.55"/>
        <stop offset="1" stop-color="var(--channel-light)" stop-opacity="0.15"/>
      </linearGradient>
      <linearGradient id="channel-up" x1="0" y1="1" x2="0" y2="0">
        <stop offset="0" stop-color="var(--channel-mid)" stop-opacity="0.55"/>
        <stop offset="1" stop-color="var(--channel-light)" stop-opacity="0.15"/>
      </linearGradient>
      <linearGradient id="rule-fade-both" x1="0" y1="0" x2="1" y2="0">
        <stop offset="0" stop-color="var(--rule)" stop-opacity="0"/>
        <stop offset="0.5" stop-color="var(--rule)"/>
        <stop offset="1" stop-color="var(--rule)" stop-opacity="0"/>
      </linearGradient>
    </defs>

    <rect class="path-upper" x="478" y="0" width="62" height="310" fill="url(#channel-down)"
          role="img" aria-label="Carved channels descending, one turning aside to the left"/>

    <text id="cover-title" class="title" text-anchor="middle">
      <tspan class="title-line title-line--lead" x="400" y="426">WEATHER OF THE HEART</tspan>
      <tspan class="title-line title-line--joiner" x="400" y="498">IS THE</tspan>
      <tspan class="title-line title-line--close" x="400" y="582">LEDGER</tspan>
    </text>
    <g class="title-rules">
      <rect x="148" y="485" width="150" height="2" fill="url(#rule-fade-both)"/>
      <rect x="514" y="485" width="150" height="2" fill="url(#rule-fade-both)"/>
    </g>

    <rect class="path-lower" x="296" y="641" width="100" height="293" fill="url(#channel-up)"
          role="img" aria-label="Carved channels descending, one turning aside to the right"/>

    <text class="byline" x="400" y="1014" text-anchor="middle">Carl &amp; Martin</text>
  </svg>
</main>
</body>
</html>
```